Letterhead, envelope, business card design

I am looking to update the communication materials for our Association and Foundation. We have two organization (Fenwick Parish Bar Association (the membership organization for lawyers and judges) and the Fenwick Parish Bar Foundation (the charitable arm of our organization).

I am attaching copies of the two organizations logos.

I am looking to update the following pieces:
* our current versions are attached for your review
* the image conveyed should be sophisticated
* Our organization color is reflex blue (I don't think the Foundation logo is correct in the versions I have)

Association:
(1) 8.5" x 11" letterhead (page 1)
(2) #10 envelopes (page 2)
(3) note cards (page 3)
(4) note card envelope (page 4)

Foundation:
(5) 8.5" x 11" letterhead (page 5)
(6) #10 envelopes (page 6)
(7) note cards (page 7)
(8) note card envelope (page 8)

Joint Association and Foundation: (using both logos)
(9) 7.5" x 10.5" (monarch) letterhead (no current version)
(10) Monarch envelope (no current version)
(11) two sided business card (page 9)

FUTURE PROJECTS:
** Membership form (tri-fold 8.5" x 11" )(page 11&12)
** Foundation overview brochure (bi-fold 8.5" x 11") (page13&14)

Target Market(s)

Lawyers and Judges

Industry/Entity Type

Business

Font styles to use
Serif

Requirements
Must have
• Street Address, City, State, Zip, Phone, web address
Nice to have
• .
Should not have
• no clip art, no additional images other than logos

```html
<!DOCTYPE html>
<html lang="en">
<head>
<meta charset="UTF-8">
<title>Fenwick Parish Bar Association Letterhead</title>
<link href="https://fonts.googleapis.com/css2?family=Open+Sans:wght@400;600&display=swap" rel="stylesheet">
<style>
  :root {
    --backdrop: #e4e4e4;
    --paper: #ffffff;
    --reflex-blue: #0b4fa3;
    --logo-blue: #1a3fa8;
    --band-text: #ffffff;
  }
  * { margin: 0; padding: 0; box-sizing: border-box; }
  html, body {
    width: 1200px;
    height: 1200px;
    overflow: hidden;
    background: var(--backdrop);
  }
  .canvas {
    width: 1200px;
    height: 1200px;
    display: flex;
    align-items: center;
    justify-content: center;
  }
  .letterhead {
    position: relative;
    width: 850px;
    height: 1100px;
    background: var(--paper);
    box-shadow: 0 2px 10px rgba(0,0,0,0.12);
    font-family: "Open Sans", sans-serif;
  }
  .masthead {
    position: absolute;
    top: 70px;
    left: 70px;
    display: flex;
    align-items: center;
    gap: 56px;
  }
  .org-name {
    display: flex;
    align-items: center;
    gap: 12px;
    color: var(--logo-blue);
    font-weight: 600;
    font-size: 17px;
    line-height: 1.25;
    letter-spacing: 0.06em;
    text-transform: uppercase;
  }
  .org-name__mark {
    flex: none;
    width: 30px;
    height: 30px;
    border-radius: 50%;
    background: var(--logo-blue);
  }
  .org-name__mark--square { border-radius: 0; }
  .contact-band {
    position: absolute;
    left: 0;
    right: 0;
    bottom: 18px;
    height: 30px;
    background: var(--reflex-blue);
    color: var(--band-text);
    display: flex;
    align-items: center;
    padding-left: 44px;
    font-size: 13.5px;
    font-weight: 400;
    letter-spacing: 0.01em;
    white-space: nowrap;
  }
  .contact-band .sep { margin: 0 7px; }
</style>
</head>
<body>
<div class="canvas">
  <article class="letterhead">
    <header class="masthead">
      <div class="org-name org-name--association">
        <span class="org-name__mark"></span>
        <span>Fenwick Parish<br>Bar Association</span>
      </div>
      <div class="org-name org-name--foundation">
        <span class="org-name__mark org-name__mark--square"></span>
        <span>Fenwick Parish<br>Bar Foundation</span>
      </div>
    </header>
    <footer class="contact-band">
      1450 Harbor Street, Suite B<span class="sep">•</span>Fenwick, IL 60912<span class="sep">•</span>P: (555) 310-4127<span class="sep">•</span>F: (555) 310-4188
    </footer>
  </article>
</div>
</body>
</html>
```